Ridge 9 Ridge Turbine Rentals Pty Ltd

We are a hire company based on the Gold Coast in Australia, we Hire out Generators to construction sites, music festivals, parties, fetes etc. Anywhere where power is required we can provide it.

Ridge 9 Ridge Turbine Rentals pty Ltd also provides all leads, distribution boards, Qualified Electricians to perform all connections. we offer refuelling services and mechanical services. 24Hr on call service - to an actual english speaking operator.

Slogan ''Power Anywhere Anytime"

Industry/Entity Type

Construction

Contact Information for Business Card

M: 0417285963
E: bookings@ridge9ridgeturbinerentals.com.au

```html
<!DOCTYPE html>
<html lang="en">
<head>
<meta charset="utf-8">
<title>Ridge 9 Ridge Turbine Rentals – Business Card</title>
<link rel="stylesheet" href="https://fonts.googleapis.com/css2?family=Quicksand:wght@400;700&display=swap">
<style>
  :root {
    --bg: #dcdcdc;
    --frame-blue: #4a86a6;
    --frame-deep: #2f6f92;
    --paper: #f2f2f0;
    --ink: #141414;
    --accent: #3d7fa3;
    --link-blue: #2d7fd0;
  }
  * { box-sizing: border-box; margin: 0; padding: 0; }
  html, body {
    width: 1200px; height: 900px; overflow: hidden;
    background: var(--bg);
    font-family: "Quicksand", sans-serif;
  }
  .stage { position: relative; width: 1200px; height: 900px; }

  .card {
    position: absolute;
    width: 560px; height: 330px;
    box-shadow: 0 6px 18px rgba(0,0,0,0.18);
  }
  .card--front { left: 90px; top: 80px; }
  .card--back  { left: 550px; top: 490px; }

  .card-frame {
    position: absolute; inset: 0;
    background: linear-gradient(135deg, var(--frame-blue), var(--frame-deep) 55%, var(--frame-blue));
  }
  .card-paper {
    position: absolute;
    left: 30px; top: 28px; right: 30px; bottom: 28px;
    background: var(--paper);
    overflow: hidden;
  }

  .brand {
    position: absolute;
    display: flex; align-items: center; gap: 14px;
  }
  .brand-mark {
    width: 54px; height: 54px;
    background: var(--accent);
    flex: none;
  }
  .brand-name {
    font-weight: 700;
    color: var(--ink);
    text-transform: uppercase;
    line-height: 1.1;
    letter-spacing: 0.5px;
    white-space: nowrap;
  }
  .card--front .brand { left: 95px; top: 105px; }
  .card--front .brand-name { font-size: 26px; }

  .card--back .brand { left: 22px; top: 105px; gap: 10px; }
  .card--back .brand-mark { width: 36px; height: 36px; }
  .card--back .brand-name { font-size: 13.5px; }

  .divider-bar {
    position: absolute;
    left: 238px; top: 80px; bottom: 0;
    width: 9px;
    background: var(--accent);
    border-radius: 5px 5px 0 0;
  }
  .contact-icon {
    position: absolute;
    left: 228px;
    width: 28px; height: 28px;
    border-radius: 50%;
    background: var(--paper);
    border: 2px solid var(--accent);
    display: flex; align-items: center; justify-content: center;
  }
  .contact-icon--phone { top: 112px; }
  .contact-icon--mail  { top: 146px; }
  .contact-icon svg { width: 14px; height: 14px; }

  .contact-list { position: absolute; left: 264px; right: 8px; top: 118px; list-style: none; }
  .contact-item {
    font-size: 9px;
    color: var(--ink);
    letter-spacing: 0;
    white-space: nowrap;
    margin-bottom: 14px;
  }
  .contact-item::after {
    content: "";
    display: block;
    width: 40px; height: 1.5px;
    background: var(--link-blue);
    margin-top: 9px;
  }
  .contact-item--phone { padding-left: 12px; }
  .contact-item--phone::after { margin-left: -4px; }
</style>
</head>
<body>
<main class="stage">

  <section class="card card--front" aria-label="Business card front">
    <div class="card-frame" role="img" aria-label="Blue border with faint world map pattern"></div>
    <div class="card-paper">
      <div class="brand">
        <span class="brand-mark"></span>
        <span class="brand-name">Ridge 9 Ridge<br>Turbine Rentals</span>
      </div>
    </div>
  </section>

  <section class="card card--back" aria-label="Business card back">
    <div class="card-frame" role="img" aria-label="Blue border with faint world map pattern"></div>
    <div class="card-paper">
      <div class="brand">
        <span class="brand-mark"></span>
        <span class="brand-name">Ridge 9 Ridge<br>Turbine Rentals</span>
      </div>

      <div class="divider-bar"></div>

      <span class="contact-icon contact-icon--phone">
        <svg viewBox="0 0 24 24" aria-hidden="true"><path fill="#3d7fa3" d="M6.6 10.8a15.1 15.1 0 0 0 6.6 6.6l2.2-2.2a1 1 0 0 1 1-.25 11.4 11.4 0 0 0 3.6.57 1 1 0 0 1 1 1V20a1 1 0 0 1-1 1A17 17 0 0 1 3 4a1 1 0 0 1 1-1h3.5a1 1 0 0 1 1 1c0 1.25.2 2.45.57 3.57a1 1 0 0 1-.25 1z"/></svg>
      </span>
      <span class="contact-icon contact-icon--mail">
        <svg viewBox="0 0 24 24" aria-hidden="true"><rect x="3" y="6" width="18" height="12" rx="1.5" fill="#3d7fa3"/><path d="M4 7l8 6 8-6" stroke="#f2f2f0" stroke-width="1.6" fill="none"/></svg>
      </span>

      <ul class="contact-list">
        <li class="contact-item contact-item--phone">0417285963</li>
        <li class="contact-item">bookings@ridge9ridgeturbinerentals.com.au</li>
      </ul>
    </div>
  </section>

</main>
</body>
</html>
```